Dynamic Templates

Our company hosts web stores for our clients. They can set up as many as they wish on our platform, and select from the stock templates we provide. We are looking to increase the number of available stock templates.

Because our users can dynamically control many of the template elements - specifically colors - they have to be flexible and abide by certain rules. These rules are spelled out in the attached documents.

Here are links to two of our most used templates:
http://fernridge.vexalcart.example/
http://stampled.vexalcart.example/

Templates need to have a landing page (what you see when first clicking one of the above links). There also needs to be a category page (what you see when clicking any category) and a product detail page (what you see when you arrive at an individual product, where there are various cart options like Buy Now or Request Info).

```html
<!DOCTYPE html>
<html lang="en">
<head>
<meta charset="utf-8">
<title>VexalCart – Distributor Storefront</title>
<link href="https://fonts.googleapis.com/css2?family=Arimo:wght@400;700&family=PT+Sans:wght@400&family=Roboto+Condensed:wght@400&display=swap" rel="stylesheet">
<style>
  :root {
    --orange: #f07d1a;
    --orange-light: #f5a01f;
    --sky: #1c9ad6;
    --ocean: #0a7ab3;
    --navy: #0b4a73;
    --ink: #111;
    --paper: #fff;
    --photo-a: #d9d4cc;
    --photo-b: #3a3a3a;
  }
  * { box-sizing: border-box; margin: 0; padding: 0; }
  html, body { width: 1200px; height: 946px; overflow: hidden; }
  body { position: relative; background: var(--paper); font-family: "Arimo", Arial, sans-serif; color: var(--ink); }
  .abs { position: absolute; }

  .brand { left: 100px; top: 21px; display: flex; align-items: center; gap: 12px; }
  .brand-dot { width: 46px; height: 46px; border-radius: 50%; background: var(--orange); }
  .brand-name { font-size: 27px; font-weight: 700; color: var(--orange); }

  .header-contact { right: 101px; top: 32px; font-size: 18px; text-decoration: underline; }

  .swoosh-top { left: 0; top: 58px; }

  .showcase { top: 140px; height: 210px; border-radius: 6px; }
  .showcase-1 { left: 168px; width: 190px; background: linear-gradient(160deg, #c9d6de, #9a3b32 80%); }
  .showcase-2 { left: 410px; width: 164px; background: linear-gradient(180deg, #4a4a4a, #1d1d1d); }
  .showcase-3 { left: 618px; width: 192px; background: linear-gradient(180deg, #7fbfe0, #e4d34a 45%, #1a1a1a 75%); }
  .showcase-4 { left: 846px; width: 196px; background: linear-gradient(180deg, #c7c7c7, #3c3c3c); }

  .intro { left: 103px; top: 400px; width: 720px; }
  .intro h1 { font-size: 27px; font-weight: 400; color: var(--orange); margin-bottom: 20px; }
  .intro h2 { font-size: 21px; font-weight: 400; color: var(--orange); margin: 14px 0 20px; }
  .intro p { font-size: 14px; line-height: 18px; margin-bottom: 18px; }

  .start-shopping { left: 953px; top: 424px; display: flex; align-items: center; gap: 3px; font-size: 16px; }

  .swoosh-bottom { left: 0; top: 695px; }
  .footer-band { left: 0; top: 740px; width: 1200px; height: 206px; background: var(--ocean); }

  .footer-nav { left: 101px; top: 760px; font-family: "PT Sans", sans-serif; font-size: 23px; line-height: 45px; }

  .quick-search { left: 932px; top: 748px; font-family: "PT Sans", sans-serif; }
  .footer-title { font-size: 23px; line-height: 30px; }
  .search-row { display: flex; align-items: center; gap: 8px; margin: 4px 0 4px; }
  .search-box { width: 178px; height: 33px; background: var(--paper); border: 1px solid #7aa9c4; }
  .search-go { font-family: "Roboto Condensed", sans-serif; font-size: 18px; }
  .contact-line { font-family: "Roboto Condensed", sans-serif; font-size: 18px; line-height: 29px; }

  .copyright { left: 0; width: 1172px; top: 913px; text-align: center; font-size: 15px; }
</style>
</head>
<body>
  <div class="abs brand">
    <span class="brand-dot"></span>
    <span class="brand-name">VexalCart</span>
  </div>
  <div class="abs header-contact">Demo User . (555) 014-2290 . info@vexalcart.example</div>

  <svg class="abs swoosh-top" width="1200" height="46" viewBox="0 0 1200 46" aria-hidden="true">
    <path d="M0 26 C300 10 700 4 1200 2 L1200 16 C700 14 300 20 0 30 Z" fill="var(--orange-light)"/>
    <path d="M0 30 C300 22 700 18 1200 20 L1200 26 C700 24 300 28 0 34 Z" fill="var(--sky)"/>
    <path d="M0 34 C300 26 700 24 1200 28 L1200 42 C700 30 300 32 0 38 Z" fill="var(--navy)"/>
  </svg>

  <div class="abs showcase showcase-1" role="img" aria-label="Product photo: adventure kit gift tin"></div>
  <div class="abs showcase showcase-2" role="img" aria-label="Product photo: black insulated cooler tote"></div>
  <div class="abs showcase showcase-3" role="img" aria-label="Product photo: colourful puzzle desk piece"></div>
  <div class="abs showcase showcase-4" role="img" aria-label="Product photo: silver and black cooler bag"></div>

  <section class="abs intro">
    <h1>Welcome To The Future of Promotional Products!</h1>
    <p>Gone are the days of searching through dog-eared catalogs or trying to make sense of complicated product websites.</p>
    <p>We do the work for you! We've taken only the very best and most current products and placed them in easy-to-use categories designed for your needs. Take a look at our selection - quality products at excellent prices.</p>
    <h2>Enjoy This Amazing New Resource</h2>
    <p>We know you don't have time to waste; so we've cut to the chase and made it simple! But keep in mind, we do have access to over a million products - so if you don't see what you're looking for or have a special theme or request, let us know - we'll find it!</p>
  </section>

  <div class="abs start-shopping">
    <svg width="26" height="26" viewBox="0 0 24 24" aria-hidden="true">
      <path d="M12 2 L14.9 8.6 L22 9.3 L16.6 14 L18.2 21 L12 17.3 L5.8 21 L7.4 14 L2 9.3 L9.1 8.6 Z" fill="#a9a9d6" stroke="#7c7cb0" stroke-width="1"/>
    </svg>
    <span>Start shopping &gt;&gt;</span>
  </div>

  <svg class="abs swoosh-bottom" width="1200" height="48" viewBox="0 0 1200 48" aria-hidden="true">
    <path d="M0 6 C400 2 800 18 1200 32 L1200 36 C800 24 400 12 0 16 Z" fill="var(--orange-light)"/>
    <path d="M0 16 C400 12 800 24 1200 36 L1200 40 C800 30 400 20 0 22 Z" fill="var(--sky)"/>
    <path d="M0 22 C400 20 800 32 1200 42 L1200 48 L0 48 Z" fill="var(--ocean)"/>
    <path d="M0 22 C400 20 800 30 1200 40 L1200 42 C800 32 400 22 0 25 Z" fill="var(--navy)"/>
  </svg>
  <div class="abs footer-band"></div>

  <nav class="abs footer-nav">
    <div>Shop By Category</div>
    <div>Shop By Price</div>
  </nav>

  <div class="abs quick-search">
    <div class="footer-title">Quick Search</div>
    <div class="search-row"><span class="search-box"></span><span class="search-go">Go</span></div>
    <div class="footer-title">Contact Us</div>
    <div class="contact-line">info@vexalcart.example</div>
    <div class="contact-line">www.vexalcart.example</div>
  </div>

  <div class="abs copyright">Copyright © 2010 . VexalCart.example V3 . All Rights Reserved.</div>
</body>
</html>
```